CGSI application splash screen

We need a 1024x768 image for use as an application splash screen.
The image will be displayed full screen on an 10 inch industrial PC 1024x768 screen while our application is launching. The image should convey that the application is "Waiting for connection to Wi-Fi access point..." and include a graphic of the industrial PC connected to the access point via an Ethernet cable. A list of troubleshooting steps should be included at the bottom of the image. The troubleshooting steps should not be the main focus of the image and should be shown in a smaller font (but still readable at 1024x768 displayed on a 10 inch screen).
I will include a mock up of the general idea of what we are looking for as well as image files for the industrial PC, a screenshot of our application to show on the PC's screen and the AP.
For general look and feel and a sense of corporate branding please review our website https://copperlanegrowingsystems.com/. The splash screen should reflect corporate branding.
Users of our application
Agriculture

```html
<!DOCTYPE html>
<html lang="en">
<head>
<meta charset="utf-8">
<title>CGSI – Waiting for connection</title>
<link href="https://fonts.googleapis.com/css2?family=Montserrat:wght@500;600;700&display=swap" rel="stylesheet">
<style>
  :root {
    --brand-green: #2db673;
    --ink-dark: #1e2a23;
    --white: #ffffff;
    --base-dark: #1c1c1c;
    --base-darker: #121212;
    --band-grey: #3b3b3b;
    --device-frame: #2a2c2e;
    --device-screen: #d9e6de;
    --ap-body: #f2f3f3;
  }
  * { margin: 0; padding: 0; box-sizing: border-box; }
  html, body { width: 1200px; height: 900px; overflow: hidden; }
  body { font-family: "Montserrat", sans-serif; background: var(--brand-green); }
  .splash { position: relative; width: 1200px; height: 900px; background: var(--brand-green); overflow: hidden; }

  .base-shape { position: absolute; left: 0; top: 0; }

  .brand { position: absolute; left: 45px; top: 32px; }
  .brand-name { font-size: 58px; font-weight: 700; color: var(--white); letter-spacing: 2px; line-height: 1; }
  .brand-sub { margin-top: 14px; padding: 3px 0 4px; border-top: 2px solid var(--white); border-bottom: 2px solid var(--white);
    font-size: 15px; font-weight: 600; color: var(--ink-dark); width: 206px; }
  .brand-sub small { display: block; font-size: 9px; font-weight: 500; text-align: right; }

  .headline { position: absolute; left: 330px; width: 700px; top: 67px; text-align: center;
    font-size: 61px; font-weight: 600; line-height: 82px; color: var(--white); }
  .headline .accent { color: var(--ink-dark); }

  .cab-computer { position: absolute; left: 57px; top: 307px; width: 270px; height: 218px;
    background: var(--device-frame); border-radius: 14px; padding: 16px 16px 34px; }
  .cab-computer .screen { width: 100%; height: 100%; background: var(--device-screen); border-radius: 3px; }

  .access-point { position: absolute; left: 1049px; top: 211px; width: 42px; height: 230px;
    background: linear-gradient(90deg, #e3e5e5, var(--ap-body) 50%, #dcdede); border-radius: 8px; }

  .cable { position: absolute; left: 0; top: 0; }

  .label { position: absolute; color: var(--white); font-weight: 600; white-space: nowrap; }
  .label .accent { color: var(--ink-dark); }
  .label-computer { left: 60px; top: 533px; width: 262px; text-align: center; font-size: 21.5px; }
  .label-cable { left: 598px; top: 443px; font-size: 22px; font-weight: 500; }
  .label-ap { left: 950px; top: 512px; width: 230px; text-align: center; font-size: 21px; font-weight: 500; }
  .label-ap .model { display: block; margin-top: 5px; font-size: 15px; color: var(--ink-dark); }

  .app-badge { position: absolute; left: 123px; top: 711px; width: 129px; height: 129px;
    background: #050505; border: 2px solid #2c2c2c; border-radius: 24px;
    display: flex; align-items: center; justify-content: center;
    color: var(--white); font-size: 32px; font-weight: 700; letter-spacing: 1px; }

  .troubleshooting { position: absolute; left: 543px; top: 667px; width: 630px; color: var(--white); }
  .troubleshooting h2 { font-size: 22px; font-weight: 700; line-height: 27px; margin-bottom: 22px; }
  .troubleshooting ul { list-style: none; font-size: 14.8px; font-weight: 500; line-height: 23.5px; }
  .troubleshooting li::before { content: "•"; margin-right: 5px; }
  .troubleshooting .steps { margin: 0 0 0 44px; }
  .troubleshooting .steps li { padding-left: 12px; text-indent: -12px; }
  .troubleshooting .steps li::before { content: "◦"; margin-right: 5px; }
</style>
</head>
<body>
<main class="splash">

  <svg class="base-shape" width="1200" height="900" viewBox="0 0 1200 900" aria-hidden="true">
    <polygon points="0,643 674,590 1200,630 1200,900 0,900" fill="var(--band-grey)"/>
    <polygon points="0,651 674,600 1200,640 1200,900 0,900" fill="var(--base-dark)"/>
    <polygon points="398,638 674,600 1200,640 1200,900 492,900" fill="var(--base-darker)"/>
  </svg>

  <div class="brand">
    <div class="brand-name">CGSI</div>
    <div class="brand-sub">Copperlane Growing<small>Systems Inc.</small></div>
  </div>

  <h1 class="headline">Waiting for<br>connection to<br><span class="accent">Wi-Fi access point...</span></h1>

  <svg class="cable" width="1200" height="900" viewBox="0 0 1200 900" aria-hidden="true">
    <path d="M330 484 L1050 484 Q1068 484 1068 466 L1068 440" fill="none" stroke="#111" stroke-width="3"/>
    <rect x="330" y="477" width="14" height="14" fill="#111"/>
    <rect x="1061" y="440" width="14" height="18" fill="#111"/>
  </svg>

  <div class="cab-computer" role="img" aria-label="Rugged tractor cab computer showing the seeding application">
    <div class="screen"></div>
  </div>
  <div class="label label-computer">Tractor cab <span class="accent">computer</span></div>

  <div class="label label-cable">Ethernet <span class="accent">cable</span></div>

  <div class="access-point" role="img" aria-label="Outdoor Wi-Fi access point with two antennas"></div>
  <div class="label label-ap">Wi-Fi Access Point<span class="model">Northmast Relay-Outdoor</span></div>

  <div class="app-badge">CGSI</div>

  <section class="troubleshooting">
    <h2>Troubleshooting steps:</h2>
    <ul>
      <li>This screen should only be visible for a short time on boot.</li>
      <li>If this screen stays visible for more than a minute:
        <ul class="steps">
          <li>Verify that when the cab computer is powered up the Wi-Fi Access Point (AP) is also powered up (indicated by green light on side of the AP).</li>
          <li>Check the Ethernet cable for damage and replace if damaged.</li>
          <li>Contact CGSI support for further assistance.</li>
        </ul>
      </li>
    </ul>
  </section>

</main>
</body>
</html>
```